Business Card - Cooperate

Business Card for Larkfield Management Consulting

Target Market(s)

Corparte - b2B

Industry/Entity Type

Management Consulting - Professional Services

Contact Information for Business Card

Company Name , Slogan , Dummy Address,

Requirements
Must have
• Reach your Full Potential

```html
<!DOCTYPE html>
<html lang="en">
<head>
<meta charset="utf-8">
<title>Larkfield Management Consulting – Business Card</title>
<link rel="stylesheet" href="https://fonts.googleapis.com/css2?family=Lato:wght@300;400;700;900&display=swap">
<style>
  :root {
    --backdrop: #011533;
    --card: #f1f1f1;
    --navy: #1c2a8c;
    --brand-blue: #1a46c4;
    --teal: #13907f;
    --green: #3fbf1f;
    --ink: #1d1d2b;
    --faint: #dfe4ee;
  }
  * { box-sizing: border-box; margin: 0; padding: 0; }
  html, body {
    width: 1200px; height: 958px; overflow: hidden;
    background: var(--backdrop);
    font-family: "Lato", sans-serif;
  }
  .sheet {
    position: relative; width: 1200px; height: 958px;
    display: flex; flex-direction: column; align-items: center;
    justify-content: center; gap: 60px;
  }
  .card {
    position: relative; width: 700px; height: 400px;
    background: var(--card); overflow: hidden;
  }

  /* Company name */
  .brand { display: flex; align-items: center; }
  .brand-dot { border-radius: 50%; background: var(--brand-blue); flex: none; }
  .brand-name {
    font-weight: 700; color: var(--brand-blue);
    letter-spacing: 0.02em; line-height: 1;
  }

  /* Front */
  .card-front .brand {
    position: absolute; left: 50%; top: 46%;
    transform: translate(-50%, -50%); gap: 16px;
  }
  .card-front .brand-dot { width: 60px; height: 60px; }
  .card-front .brand-name { font-size: 74px; }
  .slogan {
    position: absolute; left: 0; right: 0; bottom: 40px;
    text-align: center; font-size: 16px; font-weight: 400;
    color: var(--teal); letter-spacing: 0.04em;
  }

  /* Back */
  .card-back .brand { position: absolute; right: 48px; top: 40px; gap: 8px; }
  .card-back .brand-dot { width: 34px; height: 34px; }
  .card-back .brand-name { font-size: 40px; }

  .backdrop-motif {
    position: absolute; right: 70px; top: 130px;
    width: 250px; height: 250px; border-radius: 50%;
    background: radial-gradient(circle, var(--card) 0%, var(--faint) 70%);
  }
  .accent-rule {
    position: absolute; left: 60px; top: 0;
    width: 4px; height: 190px; background: var(--navy);
  }
  .accent-rule.short { top: auto; bottom: 0; height: 34px; }

  .contact { position: absolute; left: 52px; top: 212px; }
  .person-name {
    font-size: 22px; color: var(--navy); text-transform: uppercase;
    font-weight: 300; letter-spacing: 0.01em;
  }
  .person-name strong { font-weight: 900; }
  .person-role { font-size: 17px; color: var(--teal); font-weight: 400; margin-top: 2px; }
  .contact-list { list-style: none; margin-top: 18px; }
  .contact-list li {
    display: flex; align-items: center; gap: 12px;
    font-size: 15px; color: var(--ink); margin-bottom: 6px;
  }
  .contact-list svg { width: 15px; height: 15px; fill: var(--teal); }
  .contact-web {
    font-size: 16px; font-weight: 900; color: var(--teal);
    letter-spacing: 0.03em; margin-top: 4px;
  }
  .dots { position: absolute; left: 74px; bottom: 12px; display: flex; align-items: center; gap: 6px; }
  .dots span { border-radius: 50%; background: var(--green); }
  .dots span:nth-child(1) { width: 18px; height: 18px; }
  .dots span:nth-child(2) { width: 14px; height: 14px; }
  .dots span:nth-child(3) { width: 9px; height: 9px; }
</style>
</head>
<body>
<main class="sheet">
  <section class="card card-front" aria-label="Business card front">
    <div class="brand">
      <span class="brand-dot"></span>
      <span class="brand-name">larkfield</span>
    </div>
    <p class="slogan">Reach your full potential</p>
  </section>

  <section class="card card-back" aria-label="Business card back">
    <div class="backdrop-motif" role="img" aria-label="Faint brand motif"></div>
    <div class="accent-rule"></div>
    <div class="brand">
      <span class="brand-dot"></span>
      <span class="brand-name">larkfield</span>
    </div>
    <div class="contact">
      <p class="person-name">Daniel <strong>Hartwell</strong></p>
      <p class="person-role">Managing Director</p>
      <ul class="contact-list">
        <li>
          <svg viewBox="0 0 16 16" aria-hidden="true"><path d="M1 5c0-2 3-3 7-3s7 1 7 3v1h-3.5V4.5h-7V6H1z M3 7h10l1.5 7h-13z M8 8.5a2.2 2.2 0 1 0 0 4.4 2.2 2.2 0 0 0 0-4.4z"/></svg>
          01632 960418
        </li>
        <li>
          <svg viewBox="0 0 16 16" aria-hidden="true"><path d="M1 3h14v10H1z M2.5 4.5 8 9l5.5-4.5z" fill-rule="evenodd"/></svg>
          admin@larkfieldconsulting.co.uk
        </li>
      </ul>
      <p class="contact-web">www.larkfieldconsulting.co.uk</p>
    </div>
    <div class="accent-rule short"></div>
    <div class="dots" aria-hidden="true"><span></span><span></span><span></span></div>
  </section>
</main>
</body>
</html>
```